Business Card Design For Office Furniture Clearance Company

Kestrel Office Clearance - our company name pretty much explains what we do, we clear offices for high end clients, mainly plc's and large international companies.

We require a nice looking business card that displays professionalism but without being too serious.

It would be nice to see just a little more than a conventional boring business card, make sure you add some flare.

Industry/Entity Type

Office Furniture

Contact Information for Business Card

CARD 1

Tom Pardew
Director
tom@kestrelofficeclearance.co.uk
m: 07700 513928

t: 01632 419063
www.kestrelofficeclearance.co.uk

Kestrel Office Clearance
Unit K4 B
3-7 Ferndale Lane
Ashcombe
Hollybridge
ZZ9 4QX

free office clearances… you cant get better than that.

CARD 2

Henry Walbrook
Director
henry@kestrelofficeclearance.co.uk
m: 07700 628157

t: 01632 419063

Kestrel Office Clearance
Unit K4 B
3-7 Ferndale Lane
Ashcombe
Hollybridge
ZZ9 4QX

Font styles to use
Sans Serif

Requirements
Must have
• A white background - as we have a blue logo.
Nice to have
• Nice use of the logo - play around with this and dissect it.

```html
<!DOCTYPE html>
<html lang="en">
<head>
<meta charset="utf-8">
<title>Kestrel Office Clearance – Business Card</title>
<link href="https://fonts.googleapis.com/css2?family=Lato:wght@400;700;900&display=swap" rel="stylesheet">
<style>
  :root {
    --page-bg: #e9e7e3;
    --card-light-top: #f4f5f6;
    --card-light-bottom: #e6e8ec;
    --brand-blue: #2f6ea3;
    --brand-blue-deep: #174a86;
    --brand-blue-mid: #23609e;
    --panel-text: #ddd4c2;
    --curve-line: #e8edf3;
  }
  html, body {
    margin: 0;
    padding: 0;
    width: 1200px;
    height: 970px;
    overflow: hidden;
    background: var(--page-bg);
    font-family: "Lato", sans-serif;
  }
  .business-card {
    position: absolute;
    left: 100px;
    top: 207px;
    width: 1000px;
    height: 556px;
    border-radius: 26px;
    overflow: hidden;
    background: linear-gradient(180deg, var(--card-light-top), var(--card-light-bottom));
    box-shadow: 0 10px 30px rgba(0,0,0,0.12);
  }
  .card-panel {
    position: absolute;
    inset: 0;
    width: 1000px;
    height: 556px;
  }
  .brand-block {
    position: absolute;
    left: 0;
    top: 162px;
    width: 474px;
    text-align: center;
  }
  .brand-dot {
    width: 190px;
    height: 190px;
    border-radius: 50%;
    background: var(--brand-blue);
    margin: 0 auto 18px;
  }
  .brand-name {
    font-weight: 900;
    font-size: 30px;
    line-height: 36px;
    color: var(--brand-blue);
    letter-spacing: -0.3px;
    margin: 0;
  }
  .contact-block {
    position: absolute;
    left: 558px;
    top: 100px;
    color: var(--panel-text);
  }
  .person-name {
    font-size: 34px;
    font-weight: 700;
    margin: 0;
    line-height: 1.1;
  }
  .person-role {
    font-size: 22px;
    margin: 2px 0 0;
  }
  .address {
    font-size: 23px;
    line-height: 28px;
    margin: 64px 0 0;
    font-style: normal;
  }
  .contact-list {
    list-style: none;
    padding: 0;
    margin: 24px 0 0;
    font-size: 23px;
    line-height: 30px;
  }
  .contact-list li {
    display: flex;
    align-items: center;
    gap: 12px;
  }
  .contact-list svg {
    width: 22px;
    height: 22px;
    flex: none;
  }
</style>
</head>
<body>
  <div class="business-card">
    <svg class="card-panel" viewBox="0 0 1000 556" aria-hidden="true">
      <defs>
        <linearGradient id="panelBlue" x1="0" y1="0" x2="1" y2="1">
          <stop offset="0" stop-color="#1d5596"/>
          <stop offset="0.5" stop-color="#23609e"/>
          <stop offset="1" stop-color="#174a86"/>
        </linearGradient>
      </defs>
      <path d="M375 0 C470 120 500 400 374 556 L1000 556 L1000 0 Z" fill="url(#panelBlue)"/>
      <path d="M400 0 C495 120 520 400 410 556" fill="none" stroke="var(--curve-line)" stroke-width="2.5" opacity="0.85"/>
    </svg>

    <div class="brand-block">
      <div class="brand-dot"></div>
      <p class="brand-name">Kestrel Office Clearance</p>
    </div>

    <div class="contact-block">
      <h1 class="person-name">Tom Pardew</h1>
      <p class="person-role">Director</p>
      <address class="address">
        Unit K4 B, 3-7 Ferndale Lane<br>
        Ashcombe, Hollybridge<br>
        ZZ9 4QX
      </address>
      <ul class="contact-list">
        <li>
          <svg viewBox="0 0 24 24"><rect x="6" y="2" width="12" height="20" rx="2" fill="none" stroke="currentColor" stroke-width="2"/><line x1="10" y1="18" x2="14" y2="18" stroke="currentColor" stroke-width="2"/></svg>
          07700 513928
        </li>
        <li>
          <svg viewBox="0 0 24 24"><path d="M6.6 10.8a15 15 0 0 0 6.6 6.6l2.2-2.2a1 1 0 0 1 1-.25 11.4 11.4 0 0 0 3.6.57 1 1 0 0 1 1 1V20a1 1 0 0 1-1 1A17 17 0 0 1 3 4a1 1 0 0 1 1-1h3.5a1 1 0 0 1 1 1c0 1.25.2 2.45.57 3.57a1 1 0 0 1-.25 1z" fill="currentColor"/></svg>
          01632 419063
        </li>
        <li>
          <svg viewBox="0 0 24 24"><rect x="2" y="5" width="20" height="14" fill="currentColor"/><path d="M2 5l10 8 10-8" fill="none" stroke="#1f5898" stroke-width="1.6"/></svg>
          tom@kestrelofficeclearance.co.uk
        </li>
        <li>
          <svg viewBox="0 0 24 24" fill="none" stroke="currentColor" stroke-width="1.6"><circle cx="12" cy="12" r="10"/><ellipse cx="12" cy="12" rx="4.5" ry="10"/><line x1="2" y1="12" x2="22" y2="12"/><path d="M4 7h16M4 17h16"/></svg>
          www.kestrelofficeclearance.co.uk
        </li>
      </ul>
    </div>
  </div>
</body>
</html>
```